Pagina Casalúmen

The Casalúmen is a company dealing with leasing and selling real estate. The current site can be accessed at www.casalumen.com.br. We intend to redesign the look of the site and for that we would like to redesign the home page and the page with information and pictures of the property. The homepage should maintain the characteristics of the current common design simple, short and straightforward. The page with the data of the properties should be accessed with two changes page as it is currently running. The search from the map by region and should be maintained.
The page containing the information of the property will provide a total of 15 small pictures that when clicked will appear in larger size. The colors to be used should be orange, blue, black and white. The map can be maintained in the current colors.
Updates

Payment guaranteed. Deadline for submission of designs April 27.

Industry/Entity Type

Real Estate

Requirements
Must have
• Search by map regions and search box
address
keep colors from the current page
phones
clean look
Nice to have
• clean look
Should not have
• We like the current page. We just want to make it compatible with modern and new design trends and monitors.

```html
<!DOCTYPE html>
<html lang="en">
<head>
<meta charset="utf-8">
<title>Casalúmen – Search Results</title>
<link href="https://fonts.googleapis.com/css2?family=Montserrat:wght@700&family=Ubuntu:wght@400;500&family=Arimo:wght@400;700&display=swap" rel="stylesheet">
<style>
:root{
  --orange:#f97a10;
  --orange-light:#fb8a22;
  --navy:#2b2d6e;
  --ink:#33334d;
  --text:#333;
  --muted:#555;
  --panel:#f3f3f3;
  --line:#e2e2e2;
  --white:#fff;
  --footer:#f4f4f4;
}
*{box-sizing:border-box;margin:0;padding:0}
html,body{width:1200px;height:1081px;overflow:hidden}
body{position:relative;background:var(--white);font-family:"Arimo",Arial,sans-serif;color:var(--text)}
.header-band{position:absolute;left:0;top:0;width:1200px;height:172px;
  background:linear-gradient(160deg,#fb8f2a 0%,#f97a10 45%,#f6700a 100%)}
.main-nav{position:absolute;left:138px;top:36px;display:flex;gap:31px;list-style:none}
.main-nav a{font-family:"Montserrat",sans-serif;font-weight:700;font-size:14.5px;color:#fff;text-decoration:none;letter-spacing:.2px}
.phone-box{position:absolute;left:737px;top:23px;width:339px;height:43px;background:rgba(80,30,0,.75);
  border-radius:2px;color:#fff;font-size:14px;display:flex;align-items:center;justify-content:center;font-family:"Arimo",sans-serif}
.phone-box b{margin-right:4px}
.phone-box .sep{margin:0 8px}
.brand{position:absolute;left:121px;top:89px;width:261px;height:120px;background:#fff;
  box-shadow:0 6px 10px rgba(0,0,0,.18);display:flex;align-items:center;justify-content:center;gap:10px}
.brand-mark{width:18px;height:18px;background:var(--orange)}
.brand-name{font-family:"Ubuntu",sans-serif;font-weight:500;font-size:32px;color:var(--navy)}
.side-menu{position:absolute;left:121px;top:227px;width:259px;list-style:none}
.side-menu li{height:36px;border-bottom:1px solid var(--line);padding-left:23px;line-height:34px}
.side-menu li:last-child{border-bottom:none}
.side-menu a{font-family:"Ubuntu",sans-serif;font-weight:500;font-size:15px;color:var(--ink);text-decoration:none}
.quick-search{position:absolute;left:121px;top:385px;width:260px;height:163px;border:1px solid var(--line);border-radius:2px}
.quick-search h2{height:38px;background:var(--orange);color:#fff;font-family:"Ubuntu",sans-serif;font-weight:500;font-size:17px;line-height:38px;padding-left:25px}
.deal-toggle{position:absolute;left:38px;top:53px;display:flex;align-items:center;font-family:"Ubuntu",sans-serif;font-weight:500;font-size:15px;color:var(--ink)}
.deal-toggle .opt{display:flex;align-items:center;gap:9px}
.deal-toggle .divider{width:1px;height:26px;background:var(--line);margin:0 14px 0 16px}
.radio{width:16px;height:16px;border-radius:50%;border:1px solid #ccc;background:#eee;display:inline-block;position:relative}
.radio.on::after{content:"";position:absolute;left:4px;top:4px;width:6px;height:6px;border-radius:50%;background:#777}
.select{position:absolute;background:#fff;border:1px solid #ddd;border-radius:2px;font-family:"Ubuntu",sans-serif;font-size:13.5px;color:#444;padding-left:11px;display:flex;align-items:center}
.select::after{content:"";position:absolute;right:12px;top:50%;margin-top:-2px;border:5px solid transparent;border-top:5px solid #888;border-bottom:none}
.quick-search .select{left:29px;top:90px;width:197px;height:33px}
.btn-buscar{position:absolute;left:30px;top:137px;width:196px;height:42px;background:#fff;border:1px solid #ddd;
  display:flex;align-items:center;justify-content:center;gap:6px;font-family:"Ubuntu",sans-serif;font-weight:500;font-size:21px;color:var(--orange)}
.results{position:absolute;left:417px;top:90px;width:661px;height:824px;border:1px solid var(--line);border-radius:2px;background:#fff}
.adv-search{height:205px;background:var(--panel);position:relative}
.section-title{font-family:"Ubuntu",sans-serif;font-weight:500;font-size:20px;color:var(--navy);letter-spacing:-.3px}
.adv-search .section-title{position:absolute;left:22px;top:14px}
.field-label{position:absolute;font-size:13.5px;color:#444}
.field{position:absolute;width:165px;height:33px;background:#fff;border:1px solid #d6d6d6;border-radius:2px}
.adv-search .select{width:165px;height:33px}
.btn-procurar{position:absolute;left:541px;top:141px;width:89px;height:34px;background:#fff;border:1px solid #e6e6e6;
  color:var(--orange);font-family:"Ubuntu",sans-serif;font-weight:500;font-size:14.5px;display:flex;align-items:center;justify-content:center}
.results .found{position:absolute;left:21px;top:220px}
.listing{position:absolute;width:310px;height:111px}
.listing .photo{position:absolute;left:0;top:0;width:146px;height:111px}
.listing dl{position:absolute;left:159px;top:3px;display:grid;grid-template-columns:51px auto;row-gap:0;font-size:11px;line-height:19px}
.listing dt{color:var(--orange)}
.listing dd{color:#333}
.site-footer{position:absolute;left:0;top:962px;width:1200px;height:119px;background:var(--footer);border-top:1px solid #e6e6e6;text-align:center}
.site-footer .address{margin-top:30px;font-size:12.5px;color:#555}
.site-footer .address b{color:#555}
.site-footer .copy{margin-top:24px;font-size:12px;color:#777}
</style>
</head>
<body>
<div class="header-band"></div>
<ul class="main-nav">
  <li><a href="#">COMPANY</a></li>
  <li><a href="#">LOCATION</a></li>
  <li><a href="#">RESTRICTED AREA</a></li>
  <li><a href="#">CONTACT US</a></li>
</ul>
<div class="phone-box"><b>LEASE</b> (48) 3210-4455<span class="sep">|</span><b>SALES</b> (48) 8420-1177</div>

<div class="brand"><span class="brand-mark"></span><span class="brand-name">Casalúmen</span></div>

<ul class="side-menu">
  <li><a href="#">List your Property</a></li>
  <li><a href="#">Information to Owner</a></li>
  <li><a href="#">Information for the Tenant</a></li>
  <li><a href="#">Request your Property</a></li>
</ul>

<div class="quick-search">
  <h2>Search for Properties</h2>
  <div class="deal-toggle">
    <span class="opt">To Buy <span class="radio"></span></span>
    <span class="divider"></span>
    <span class="opt">To Rent <span class="radio on"></span></span>
  </div>
  <div class="select">All Properties</div>
  <div class="btn-buscar">Buscar
    <svg width="22" height="22" viewBox="0 0 22 22"><circle cx="9" cy="9" r="6.5" fill="none" stroke="#f97a10" stroke-width="3"/><line x1="13.5" y1="13.5" x2="20" y2="20" stroke="#f97a10" stroke-width="3.5" stroke-linecap="round"/></svg>
  </div>
</div>

<main class="results">
  <section class="adv-search">
    <h1 class="section-title">Advanced Search</h1>
    <span class="field-label" style="left:26px;top:65px">Código:</span>
    <div class="field" style="left:98px;top:57px"></div>
    <span class="field-label" style="left:292px;top:65px">Bairro:</span>
    <div class="field" style="left:350px;top:57px"></div>
    <span class="field-label" style="left:26px;top:107px">Tipo:</span>
    <div class="select" style="left:98px;top:99px">All Properties</div>
    <span class="field-label" style="left:292px;top:107px">Cidade:</span>
    <div class="select" style="left:350px;top:99px">All Properties</div>
    <span class="field-label" style="left:26px;top:149px">Endereço:</span>
    <div class="field" style="left:98px;top:140px"></div>
    <span class="field-label" style="left:292px;top:149px">Região:</span>
    <div class="field" style="left:350px;top:140px"></div>
    <div class="btn-procurar">Procurar</div>
  </section>

  <h2 class="section-title found">Found 8 properties:</h2>

  <article class="listing" style="left:22px;top:265px"><div class="photo" role="img" aria-label="Photo of a hillside house among trees" style="background:linear-gradient(#b9c7d6,#6f7f5a 60%,#4d5b3a)"></div>
    <dl><dt>Código:</dt><dd>S00691</dd><dt>Tipo:</dt><dd>Sala Comercial</dd><dt>Quartos:</dt><dd>0</dd><dt>Bairro:</dt><dd>Centro</dd><dt>Cidade:</dt><dd>Florianopolis</dd><dt>Valor:</dt><dd>R$ 750,00</dd></dl></article>
  <article class="listing" style="left:346px;top:265px"><div class="photo" role="img" aria-label="Photo of a two-storey street building" style="background:linear-gradient(#c9ced6,#a9a39b 50%,#7b7670)"></div>
    <dl><dt>Código:</dt><dd>S00691</dd><dt>Tipo:</dt><dd>Sala Comercial</dd><dt>Quartos:</dt><dd>0</dd><dt>Bairro:</dt><dd>Centro</dd><dt>Cidade:</dt><dd>Florianopolis</dd><dt>Valor:</dt><dd>R$ 750,00</dd></dl></article>
  <article class="listing" style="left:22px;top:397px"><div class="photo" role="img" aria-label="Photo of a house behind a large tree" style="background:linear-gradient(#6e8d4e,#4f6a35 55%,#8a8a80)"></div>
    <dl><dt>Código:</dt><dd>S00691</dd><dt>Tipo:</dt><dd>Sala Comercial</dd><dt>Quartos:</dt><dd>0</dd><dt>Bairro:</dt><dd>Centro</dd><dt>Cidade:</dt><dd>Florianopolis</dd><dt>Valor:</dt><dd>R$ 750,00</dd></dl></article>
  <article class="listing" style="left:346px;top:397px"><div class="photo" role="img" aria-label="Photo of a white apartment block" style="background:linear-gradient(#cfd6dd,#b8b8b6 55%,#6d7560)"></div>
    <dl><dt>Código:</dt><dd>S00691</dd><dt>Tipo:</dt><dd>Sala Comercial</dd><dt>Quartos:</dt><dd>0</dd><dt>Bairro:</dt><dd>Centro</dd><dt>Cidade:</dt><dd>Florianopolis</dd><dt>Valor:</dt><dd>R$ 750,00</dd></dl></article>
  <article class="listing" style="left:22px;top:528px"><div class="photo" role="img" aria-label="Aerial photo of a waterfront condominium" style="background:linear-gradient(#4f6a42,#7a8670 45%,#1f3a5a 70%,#183050)"></div>
    <dl><dt>Código:</dt><dd>S00691</dd><dt>Tipo:</dt><dd>Sala Comercial</dd><dt>Quartos:</dt><dd>0</dd><dt>Bairro:</dt><dd>Centro</dd><dt>Cidade:</dt><dd>Florianopolis</dd><dt>Valor:</dt><dd>R$ 750,00</dd></dl></article>
  <article class="listing" style="left:346px;top:528px"><div class="photo" role="img" aria-label="Photo of a white three-storey building with cars" style="background:linear-gradient(#c6ccd3,#b3b1ad 55%,#5e5e5e)"></div>
    <dl><dt>Código:</dt><dd>S00691</dd><dt>Tipo:</dt><dd>Sala Comercial</dd><dt>Quartos:</dt><dd>0</dd><dt>Bairro:</dt><dd>Centro</dd><dt>Cidade:</dt><dd>Florianopolis</dd><dt>Valor:</dt><dd>R$ 750,00</dd></dl></article>
  <article class="listing" style="left:22px;top:660px"><div class="photo" role="img" aria-label="Photo of a white house with a covered porch" style="background:linear-gradient(#c4d2e0,#dcdcd8 45%,#8a7c68)"></div>
    <dl><dt>Código:</dt><dd>S00691</dd><dt>Tipo:</dt><dd>Sala Comercial</dd><dt>Quartos:</dt><dd>0</dd><dt>Bairro:</dt><dd>Centro</dd><dt>Cidade:</dt><dd>Florianopolis</dd><dt>Valor:</dt><dd>R$ 750,00</dd></dl></article>
  <article class="listing" style="left:346px;top:660px"><div class="photo" role="img" aria-label="Photo of a tall downtown building on a street" style="background:linear-gradient(#b9c0c8,#a39a78 50%,#6a6660)"></div>
    <dl><dt>Código:</dt><dd>S00691</dd><dt>Tipo:</dt><dd>Sala Comercial</dd><dt>Quartos:</dt><dd>0</dd><dt>Bairro:</dt><dd>Centro</dd><dt>Cidade:</dt><dd>Florianopolis</dd><dt>Valor:</dt><dd>R$ 750,00</dd></dl></article>
</main>

<footer class="site-footer">
  <p class="address"><b>Rua Antônio Vieira, 48 - Corner with Paulo Mendes Street - Downtown - Florianópolis</b> &nbsp; <b>CEP:</b> 88015-210 <b>- Fax: (48)</b> 3340-2290</p>
  <p class="copy">© 2013 - Casalúmen - All Rights Reserved.</p>
</footer>
</body>
</html>
```